Women sanitary pads, company name: Vela, need package design

We need 2 package designs for our women sanitary pads line. We want something relaxing, feminine and bold. The design can be the same for both packages. We just want the smaller one to have a white background since it is for day time and the bigger one to have a black background since it is for night time.

The name of the company is Vela = Quietly Luminous, because many girls and women still ashamed of their menstrual period, we wanted to create something that would make them confortable with themselves and not to feel alone. The final design should communicate freedom, confidence, and being feminine.

Target Market(s)

Women from 13 years to 45 years.

Industry/Entity Type

It Company

Font styles to use
Serif
Sans Serif
Script

Colors

Designer to choose colors to be used in the design.

Requirements
Must have
• 4 harmonic feminine and relaxing colors.
• I uploaded 2 images . One is about the the flow chart and the other one is about the steps on how to use the pads. They do not have to be exactly the same. That is just an ideia.
• That is also the recycle symbol that we'd like to have.
Nice to have
• I'd like to see something simple, harmonic and eye-catching.
Should not have
• More than 4 colors.

```html
<!DOCTYPE html>
<html lang="en">
<head>
<meta charset="utf-8">
<title>Vela — Package Design</title>
<link href="https://fonts.googleapis.com/css2?family=Montserrat:wght@300;800&family=Mulish:ital,wght@0,300;1,300;1,400&family=Great+Vibes&family=Kalam:wght@700&display=swap" rel="stylesheet">
<style>
  :root {
    --crimson: #e2062f;
    --ink: #1e1e1e;
    --rose: #e0439a;
    --rose-soft: #f6d3e6;
    --plum: #a3127c;
    --night: #140208;
    --band: #f4f4f4;
    --label: #8a8a8a;
  }
  * { margin: 0; padding: 0; box-sizing: border-box; }
  html, body { width: 1200px; height: 1200px; overflow: hidden; background: #fff; }
  .board { position: relative; width: 1200px; height: 1200px; font-family: "Mulish", sans-serif; }
  .section-label {
    position: absolute; left: 85px; font-family: "Montserrat", sans-serif; font-weight: 300;
    font-size: 19px; letter-spacing: 0.5px; color: var(--label);
  }
  .band { position: absolute; left: 0; top: 290px; width: 1200px; height: 462px; background: var(--band); }

  .brand-mark { position: absolute; left: 0; top: 52px; width: 1200px; text-align: center; }
  .brand-name {
    font-family: "Montserrat", sans-serif; font-weight: 800; font-size: 150px; line-height: 1;
    color: var(--crimson); letter-spacing: -3px;
  }
  .brand-tagline {
    font-family: "Kalam", cursive; font-weight: 700; font-size: 38px; color: var(--ink); margin-top: 4px;
  }

  .pack { position: absolute; width: 520px; height: 416px; overflow: hidden; transform-origin: top left; }
  .pack--day { background: radial-gradient(120% 100% at 30% 40%, #fff 0%, #fff 55%, #fdf1f7 100%); }
  .pack--night { background: radial-gradient(120% 100% at 30% 40%, #1c040d 0%, var(--night) 60%, #0e0105 100%); }
  .pack--preview { border-radius: 18px; }

  .pack__pattern { position: absolute; inset: 0; }
  .pack--day .pack__pattern {
    background:
      radial-gradient(40px 30px at 12% 14%, rgba(224,67,154,0.07), transparent 70%),
      radial-gradient(50px 36px at 55% 20%, rgba(224,67,154,0.07), transparent 70%),
      radial-gradient(46px 34px at 8% 80%, rgba(224,67,154,0.07), transparent 70%),
      radial-gradient(54px 40px at 50% 88%, rgba(224,67,154,0.07), transparent 70%);
  }
  .pack--night .pack__pattern {
    background:
      radial-gradient(40px 30px at 12% 14%, rgba(163,18,124,0.14), transparent 70%),
      radial-gradient(50px 36px at 55% 20%, rgba(163,18,124,0.14), transparent 70%),
      radial-gradient(46px 34px at 8% 80%, rgba(163,18,124,0.14), transparent 70%),
      radial-gradient(54px 40px at 50% 88%, rgba(163,18,124,0.14), transparent 70%);
  }

  .pack__figure { position: absolute; left: 300px; top: 20px; width: 220px; height: 380px; }
  .pack--day .pack__figure {
    background:
      radial-gradient(30% 12% at 50% 18%, rgba(224,67,154,0.30), transparent 100%),
      radial-gradient(22% 40% at 46% 55%, rgba(224,67,154,0.26), transparent 100%),
      radial-gradient(45% 55% at 50% 50%, rgba(224,67,154,0.12), transparent 100%);
  }
  .pack--night .pack__figure {
    background:
      radial-gradient(35% 18% at 45% 22%, rgba(196,21,127,0.45), transparent 100%),
      radial-gradient(28% 40% at 52% 60%, rgba(196,21,127,0.35), transparent 100%),
      radial-gradient(50% 55% at 50% 50%, rgba(163,18,124,0.18), transparent 100%);
  }

  .pack__name {
    position: absolute; left: 37px; top: 52px; font-family: "Montserrat", sans-serif; font-weight: 800;
    font-size: 80px; line-height: 1; color: var(--crimson); letter-spacing: -2px;
  }
  .pack__tagline { position: absolute; left: 90px; top: 128px; font-style: italic; font-size: 16px; }
  .pack--day .pack__tagline, .pack--day .pack__count { color: var(--ink); }
  .pack--night .pack__tagline, .pack--night .pack__count { color: #fff; }

  .pack__title {
    position: absolute; left: 22px; top: 194px; font-family: "Great Vibes", cursive; font-size: 56px;
    line-height: 1; white-space: nowrap;
  }
  .pack--day .pack__title { color: var(--rose); }
  .pack--night .pack__title { color: var(--plum); }

  .pack__rule { position: absolute; left: 272px; top: 242px; width: 248px; height: 2px; }
  .pack--day .pack__rule { background: var(--rose); }
  .pack--night .pack__rule { background: var(--plum); }

  .pack__pad {
    position: absolute; left: 30px; top: 278px; width: 56px; height: 82px; border-radius: 26px 26px 18px 18px;
    background: linear-gradient(160deg, #fbe3ef, #e58fbf);
  }
  .pack__badge {
    position: absolute; left: 68px; top: 268px; width: 112px; height: 66px; border-radius: 50%;
    transform: rotate(-8deg); display: flex; flex-direction: column; justify-content: center;
    padding-left: 12px; color: #fff; font-family: "Montserrat", sans-serif; font-weight: 300;
    font-size: 15px; line-height: 0.95;
  }
  .pack--day .pack__badge { background: var(--rose); }
  .pack--night .pack__badge { background: var(--plum); }

  .pack__claim { position: absolute; left: 98px; top: 344px; font-style: italic; font-size: 14px; }
  .pack--day .pack__claim { color: var(--rose); }
  .pack--night .pack__claim { color: #c94aa0; }

  .pack__count { position: absolute; left: 32px; top: 380px; font-style: italic; font-size: 13px; display: flex; align-items: center; gap: 4px; }
  .flow-drops { display: inline-flex; }
</style>
</head>
<body>
<div class="board">
  <div class="section-label" style="top:58px">LOGO</div>
  <div class="brand-mark">
    <div class="brand-name">Vela</div>
    <div class="brand-tagline">Quietly Luminous!</div>
  </div>

  <div class="band"></div>
  <div class="section-label" style="top:315px">FRONT DESIGN</div>
  <div class="section-label" style="top:794px">PREVIEW</div>

  <!-- Front: day -->
  <div class="pack pack--day" style="left:148px; top:356px; transform:scale(0.802)">
    <div class="pack__pattern" role="img" aria-label="Faint pattern of hearts, lips, crowns and flowers"></div>
    <div class="pack__figure" role="img" aria-label="Single-line drawing of a woman with arms raised in joy"></div>
    <div class="pack__name">Vela</div>
    <div class="pack__tagline">Quietly Luminous!</div>
    <div class="pack__title">Happy Day</div>
    <div class="pack__rule"></div>
    <div class="pack__pad" role="img" aria-label="Illustration of a sanitary pad"></div>
    <div class="pack__badge"><span>maximum</span><span>protection</span></div>
    <div class="pack__claim">breathable, strong and flexible</div>
    <div class="pack__count">5 pads ultra thin | regular flow
      <svg class="flow-drops" width="34" height="12" viewBox="0 0 34 12" fill="none" stroke="#e0439a" stroke-width="1.4"><path d="M5 1 C7 4 9 6 9 8 A4 4 0 0 1 1 8 C1 6 3 4 5 1Z"/><path d="M16 1 C18 4 20 6 20 8 A4 4 0 0 1 12 8 C12 6 14 4 16 1Z"/><path d="M27 1 C29 4 31 6 31 8 A4 4 0 0 1 23 8 C23 6 25 4 27 1Z"/></svg>
    </div>
  </div>

  <!-- Front: night -->
  <div class="pack pack--night" style="left:614px; top:340px; transform:scale(0.845)">
    <div class="pack__pattern" role="img" aria-label="Faint pattern of hearts, lips, crowns and flowers"></div>
    <div class="pack__figure" role="img" aria-label="Single-line drawing of a woman sleeping on a pillow"></div>
    <div class="pack__name">Vela</div>
    <div class="pack__tagline">Quietly Luminous!</div>
    <div class="pack__title">Good Night</div>
    <div class="pack__rule"></div>
    <div class="pack__pad" role="img" aria-label="Illustration of a sanitary pad"></div>
    <div class="pack__badge"><span>maximum</span><span>protection</span></div>
    <div class="pack__claim">breathable, strong and flexible</div>
    <div class="pack__count">5 pads ultra thin | heavy flow
      <svg class="flow-drops" width="56" height="12" viewBox="0 0 56 12" fill="none" stroke="#c4157f" stroke-width="1.4"><path d="M5 1 C7 4 9 6 9 8 A4 4 0 0 1 1 8 C1 6 3 4 5 1Z"/><path d="M16 1 C18 4 20 6 20 8 A4 4 0 0 1 12 8 C12 6 14 4 16 1Z"/><path d="M27 1 C29 4 31 6 31 8 A4 4 0 0 1 23 8 C23 6 25 4 27 1Z"/><path d="M38 1 C40 4 42 6 42 8 A4 4 0 0 1 34 8 C34 6 36 4 38 1Z"/><path d="M49 1 C51 4 53 6 53 8 A4 4 0 0 1 45 8 C45 6 47 4 49 1Z"/></svg>
    </div>
  </div>

  <!-- Preview: day -->
  <div class="pack pack--day pack--preview" style="left:164px; top:844px; transform:scale(0.73); box-shadow:0 0 0 1px #eee">
    <div class="pack__pattern" role="img" aria-label="Faint pattern of hearts, lips, crowns and flowers"></div>
    <div class="pack__figure" role="img" aria-label="Single-line drawing of a woman with arms raised in joy"></div>
    <div class="pack__name">Vela</div>
    <div class="pack__tagline">Quietly Luminous!</div>
    <div class="pack__title">Happy Day</div>
    <div class="pack__rule"></div>
    <div class="pack__pad" role="img" aria-label="Illustration of a sanitary pad"></div>
    <div class="pack__badge"><span>maximum</span><span>protection</span></div>
    <div class="pack__claim">breathable, strong and flexible</div>
    <div class="pack__count">5 pads ultra thin | regular flow
      <svg class="flow-drops" width="34" height="12" viewBox="0 0 34 12" fill="none" stroke="#e0439a" stroke-width="1.4"><path d="M5 1 C7 4 9 6 9 8 A4 4 0 0 1 1 8 C1 6 3 4 5 1Z"/><path d="M16 1 C18 4 20 6 20 8 A4 4 0 0 1 12 8 C12 6 14 4 16 1Z"/><path d="M27 1 C29 4 31 6 31 8 A4 4 0 0 1 23 8 C23 6 25 4 27 1Z"/></svg>
    </div>
  </div>

  <!-- Preview: night -->
  <div class="pack pack--night pack--preview" style="left:636px; top:828px; transform:scale(0.774)">
    <div class="pack__pattern" role="img" aria-label="Faint pattern of hearts, lips, crowns and flowers"></div>
    <div class="pack__figure" role="img" aria-label="Single-line drawing of a woman sleeping on a pillow"></div>
    <div class="pack__name">Vela</div>
    <div class="pack__tagline">Quietly Luminous!</div>
    <div class="pack__title">Good Night</div>
    <div class="pack__rule"></div>
    <div class="pack__pad" role="img" aria-label="Illustration of a sanitary pad"></div>
    <div class="pack__badge"><span>maximum</span><span>protection</span></div>
    <div class="pack__claim">breathable, strong and flexible</div>
    <div class="pack__count">5 pads ultra thin | heavy flow
      <svg class="flow-drops" width="56" height="12" viewBox="0 0 56 12" fill="none" stroke="#c4157f" stroke-width="1.4"><path d="M5 1 C7 4 9 6 9 8 A4 4 0 0 1 1 8 C1 6 3 4 5 1Z"/><path d="M16 1 C18 4 20 6 20 8 A4 4 0 0 1 12 8 C12 6 14 4 16 1Z"/><path d="M27 1 C29 4 31 6 31 8 A4 4 0 0 1 23 8 C23 6 25 4 27 1Z"/><path d="M38 1 C40 4 42 6 42 8 A4 4 0 0 1 34 8 C34 6 36 4 38 1Z"/><path d="M49 1 C51 4 53 6 53 8 A4 4 0 0 1 45 8 C45 6 47 4 49 1Z"/></svg>
    </div>
  </div>
</div>
</body>
</html>
```